Southport Billboard for Hiring more CDL drivers

I need a catch design for a bill board (size 10ft by 36 ft) to catch the attention for semi truck drivers.
In the design I want it to include:
-My company logo along with my website(brisklanefreighters.com) and my number(503-217-6095) for contact info.
-I also need it to say earn up to $90,000 a year
-I will send a few photos to choose from
-I need the logo to look clean and simple! I don't want it to be cluttered just clean, simple and catchy.!

Target Market(s)

CDL Class A holders
Semi Truck Drivers

Industry/Entity Type

Trucking Company

Font styles to use
Other font styles liked:
• a font to match my logo

Requirements
Must have
• "Make up to $90,000"
"brisklanefreighters.com"
"503-217-6095"

```html
<!DOCTYPE html>
<html lang="en">
<head>
<meta charset="utf-8">
<title>Brisk Lane Freighters – Driver Hiring Billboard</title>
<link rel="stylesheet" href="https://fonts.googleapis.com/css2?family=Oswald:wght@400;700&family=Rubik+Dirt&family=Montserrat:wght@700&display=swap">
<style>
  :root {
    --page-bg: #f1f1f1;
    --board-green: #1e2520;
    --ink-white: #ffffff;
    --sky-top: #9fc3ea;
    --sky-low: #d9c9c0;
    --ground: #8f8b86;
  }
  html, body {
    margin: 0;
    padding: 0;
    width: 1133px;
    height: 1200px;
    overflow: hidden;
    background: var(--page-bg);
  }
  .billboard {
    position: absolute;
    left: 36px;
    top: 438px;
    width: 1060px;
    height: 323px;
    background: var(--board-green);
    box-shadow: 0 6px 40px rgba(0,0,0,0.22);
    overflow: hidden;
    color: var(--ink-white);
  }
  .truck-photo {
    position: absolute;
    inset: 0;
    width: 100%;
    height: 100%;
  }
  .brand-name {
    position: absolute;
    left: 26px;
    top: 30px;
    width: 220px;
    font-family: "Oswald", sans-serif;
    font-weight: 700;
    font-size: 46px;
    line-height: 1.02;
    text-transform: uppercase;
    letter-spacing: 1px;
    color: var(--ink-white);
  }
  .headline-lead {
    position: absolute;
    left: 340px;
    top: 20px;
    font-family: "Oswald", sans-serif;
    font-weight: 400;
    font-size: 78px;
    line-height: 1;
    letter-spacing: -1px;
    transform: scaleX(0.82);
    transform-origin: left top;
    white-space: nowrap;
  }
  .headline-amount {
    position: absolute;
    left: 308px;
    top: 86px;
    font-family: "Rubik Dirt", sans-serif;
    font-size: 104px;
    line-height: 1;
    white-space: nowrap;
    transform: scaleX(0.86);
    transform-origin: left top;
  }
  .headline-amount .currency {
    font-family: "Oswald", sans-serif;
    font-weight: 400;
    font-size: 44px;
    vertical-align: 42px;
    margin-right: 2px;
  }
  .contact-phone {
    position: absolute;
    left: 34px;
    top: 196px;
    font-family: "Rubik Dirt", sans-serif;
    font-size: 86px;
    line-height: 1;
    white-space: nowrap;
    transform: scaleX(0.88);
    transform-origin: left top;
  }
  .contact-web {
    position: absolute;
    left: 27px;
    top: 280px;
    font-family: "Montserrat", sans-serif;
    font-weight: 700;
    font-size: 30px;
    line-height: 1;
    white-space: nowrap;
  }
</style>
</head>
<body>
  <section class="billboard">
    <svg class="truck-photo" viewBox="0 0 1060 323" preserveAspectRatio="none" role="img" aria-label="Photo of a teal semi truck with a wide load banner hauling an orange excavator on a lowboy trailer at dusk">
      <defs>
        <linearGradient id="photoTones" x1="0" y1="0" x2="0" y2="1">
          <stop offset="0" stop-color="var(--sky-top)"/>
          <stop offset="0.45" stop-color="var(--sky-low)"/>
          <stop offset="0.7" stop-color="#5f9aa8"/>
          <stop offset="1" stop-color="var(--ground)"/>
        </linearGradient>
      </defs>
      <polygon points="618,0 1060,0 1060,323 809,323" fill="url(#photoTones)"/>
    </svg>

    <div class="brand-name">Brisk Lane<br>Freighters</div>

    <div class="headline-lead">EARN UPTO</div>
    <div class="headline-amount"><span class="currency">$</span>90,000</div>

    <div class="contact-phone">503-217-6095</div>
    <div class="contact-web">www.brisklanefreighters.com</div>
  </section>
</body>
</html>
```